Foodcard Package Design for 10ml Food Enhancer

I have developed a product with a friend that we will be selling later this year, it is a liquid that comes in a small 10ml or 20ml bottle for sale in shops (a flavour enhancer).

A small cardboard sized backer of approximate size "A5" is the best packaging for this product.

i have attached an example of what I am looking for - the front will hold the bottle inside a small plastic case, and the back will be how to use the product / instructions.

What I am looking for is:
Strong graphic design skills to capture customers attention
Good layout of "how to use" instructions so it is clear for customer to understand
Similar "feel" to attached document as guide only

(Note: I will add the words myself, the graphics is all I need. When you design the front & back you will add Lorem ipsom text to display position of text only).

Target Market(s)

Retail & Restaurant industry

Industry/Entity Type

Retail

Font styles to use
Serif

Requirements
Must have
• Captures customers attention, high impact, sophisticated
Nice to have
• Colour, cutting edge look
Should not have
• Not cheap looking

```html
<!DOCTYPE html>
<html lang="en">
<head>
<meta charset="utf-8">
<title>The Final Flavour Note – Backer Card</title>
<link href="https://fonts.googleapis.com/css2?family=Roboto+Slab:wght@300;400&display=swap" rel="stylesheet">
<style>
  :root{
    --brand-blue:#1a8fc0;
    --card-white:#ffffff;
    --ink:#222222;
    --outline:#1e1e1e;
    --window-grey:#a9a9a9;
    --page:#ffffff;
  }
  *{box-sizing:border-box;margin:0;padding:0}
  html,body{width:1200px;height:895px;overflow:hidden;background:var(--page)}
  body{position:relative;font-family:"Roboto Slab",Georgia,serif;font-weight:300}

  .card{position:absolute;top:44px;width:450px;height:798px;border:2px solid var(--outline);border-radius:24px;overflow:hidden}
  .card--front{left:116px;background:var(--card-white)}
  .card--back{left:627px;background:var(--brand-blue);color:#fff}

  .hang-hole{position:absolute;left:176px;top:28px;width:96px;height:34px}

  .blister-window{position:absolute;left:326px;top:82px;width:101px;height:696px;border:2px solid var(--window-grey);border-radius:40px}

  /* front */
  .front-column{position:absolute;left:47px;top:0;width:238px;text-align:center;color:var(--brand-blue);text-transform:uppercase}
  .brand-mark{position:absolute;left:0;top:150px;width:238px;text-align:center}
  .brand-mark__dot{display:block;width:30px;height:30px;border-radius:50%;background:var(--ink);margin:0 auto 12px}
  .brand-mark__name{font-size:27px;line-height:30px;font-weight:400;color:var(--ink)}
  .product-title{position:absolute;left:0;top:320px;width:238px;font-size:21px;line-height:28px;font-weight:300}
  .uses{position:absolute;left:0;top:415px;width:238px;list-style:none;border-top:2px solid var(--brand-blue)}
  .uses li{display:flex;align-items:center;justify-content:center;height:46px;border-bottom:2px solid var(--brand-blue);font-size:17px;line-height:22px}
  .uses li.uses__lead{height:94px}

  /* back */
  .back-symbol{position:absolute;left:195px;top:110px;width:60px;height:60px;border-radius:50%;background:#fff}
  .back-name{position:absolute;left:0;top:193px;width:100%;text-align:center;font-size:38px;line-height:40px;font-weight:400;text-transform:uppercase}
  .rule{position:absolute;left:179px;width:92px;height:4px;background:#fff}
  .rule--upper{top:284px}
  .rule--lower{top:354px}
  .back-subtitle{position:absolute;left:0;top:300px;width:100%;text-align:center;font-size:20px;line-height:22px;text-transform:uppercase}
  .options-heading{position:absolute;left:0;top:376px;width:100%;text-align:center;font-size:20px;line-height:24px;text-transform:uppercase}
  .options{position:absolute;top:414px;width:177px;font-size:12.5px;line-height:17.2px}
  .options--left{left:40px}
  .options--right{left:244px}
  .option{margin-bottom:17px}
  .option h3{font-size:12.5px;font-weight:300;text-transform:uppercase}
  .option p{text-align:justify}
</style>
</head>
<body>

<section class="card card--front" aria-label="Front of backer card">
  <svg class="hang-hole" viewBox="0 0 96 34" aria-hidden="true">
    <path d="M10 14 H36 A12 12 0 0 1 60 14 H86 A9 9 0 0 1 86 32 H10 A9 9 0 0 1 10 14 Z" fill="#fff" stroke="#1e1e1e" stroke-width="2"/>
  </svg>

  <div class="front-column">
    <div class="brand-mark">
      <span class="brand-mark__dot"></span>
      <p class="brand-mark__name">The Final<br>Flavour Note</p>
    </div>
    <h1 class="product-title">Hollowmere Oak<br>Wine Barrel Wood<br>Extracts</h1>
    <ul class="uses">
      <li class="uses__lead">Add to boiling water<br>for farmhouse style<br>vegetables</li>
      <li>Mashed Potatoes</li>
      <li>Rice</li>
      <li>Sauces</li>
      <li>Stews Casseroles</li>
      <li>Perfect Whisky</li>
    </ul>
  </div>

  <div class="blister-window" aria-label="Clear window for bottle"></div>
</section>

<section class="card card--back" aria-label="Back of backer card">
  <svg class="hang-hole" viewBox="0 0 96 34" aria-hidden="true">
    <path d="M10 14 H36 A12 12 0 0 1 60 14 H86 A9 9 0 0 1 86 32 H10 A9 9 0 0 1 10 14 Z" fill="#fff" stroke="#1e1e1e" stroke-width="2"/>
  </svg>

  <span class="back-symbol" aria-hidden="true"></span>
  <h2 class="back-name">The Final<br>Flavour Note</h2>
  <span class="rule rule--upper"></span>
  <p class="back-subtitle">Hollowmere Oak Wine<br>Barrel Wood Extracts</p>
  <span class="rule rule--lower"></span>
  <h3 class="options-heading">Try these easy options</h3>

  <div class="options options--left">
    <div class="option">
      <h3>Mashed Potatoes</h3>
      <p>Add wooded earth and charm to mashed potatoes. Can be used in place of cream &amp; butter. Add 2 drops to your bowl of mashed potatoes for an earth charm flavour.</p>
    </div>
    <div class="option">
      <h3>Rice</h3>
      <p>Or apply to boiled rice for a smoky plume”. Once rice is cooked stir in 2 drops and experience the differ&shy;ence</p>
    </div>
    <div class="option">
      <h3>Sauces</h3>
      <p>Do you make your own sauces? Stir in 2 drops to your sauces for an extra level of depth.</p>
    </div>
  </div>

  <div class="options options--right">
    <div class="option">
      <h3>Stews Casseroles</h3>
      <p>Add 2 drops to your bowl of mashed potatoes for a smokey charm</p>
    </div>
    <div class="option">
      <h3>Perfect Whisky</h3>
      <p>Mix with water and freeze into ice cube trays. Add cubes to torn ordinary whisky into a premium aged whisky</p>
    </div>
  </div>
</section>

</body>
</html>
```